Hey Lunagraf, this time I go to you in direct demand :)
We need a Facebook Event Cover (High definition) :
- Name of the party "VELVET TIDE"
- Date of the party "Samedi 25 novembre"
- Place of the party "Brume7" (use logo please)
- DJ's: "K-Lenz + MV"
- Style of the flyer : Vintage
- Inspiration : Old vintage Ads, old vintage objects linked to music, inspiration on google images "Vintage party" "Retro Vintage party", should be really stylish :)
- Colors : You decide, you can try, pastel colors ?

```html
<!DOCTYPE html>
<html lang="fr">
<head>
<meta charset="utf-8">
<title>Velvet Tide – Music Party</title>
<link rel="stylesheet" href="https://fonts.googleapis.com/css2?family=Titan+One&family=Bungee&family=Oswald:wght@700&display=swap">
<style>
  :root {
    --artboard: #6d6d6d;
    --cream: #fef7cf;
    --ray: #e6dfa6;
    --pink: #f2aac8;
    --plum: #6a3a80;
    --sky: #b3cfe8;
    --sky-light: #d6e7f7;
    --lilac: #a07cb8;
    --vinyl: #432551;
    --lemon: #f3ee66;
  }
  html, body {
    margin: 0;
    width: 1200px;
    height: 1117px;
    overflow: hidden;
    background: var(--artboard);
  }
  .canvas { display: block; width: 1200px; height: 1117px; }
  .title {
    font-family: "Titan One", sans-serif;
    text-anchor: middle;
    stroke-linejoin: round;
    paint-order: stroke fill;
  }
  .title--top { font-size: 176px; letter-spacing: 4px; }
  .title--main { font-size: 270px; letter-spacing: 6px; }
  .title-fill--top { fill: var(--sky); stroke: var(--plum); stroke-width: 20px; }
  .title-fill--main { fill: var(--cream); stroke: var(--plum); stroke-width: 24px; }
  .title-shadow { fill: var(--plum); stroke: var(--plum); stroke-width: 24px; }
  .subtitle {
    font-family: "Bungee", sans-serif;
    font-size: 128px;
    text-anchor: middle;
    fill: var(--plum);
    stroke: var(--cream);
    stroke-width: 8px;
    paint-order: stroke fill;
  }
  .record-text {
    font-family: "Oswald", sans-serif;
    font-weight: 700;
    font-size: 60px;
    fill: var(--cream);
    letter-spacing: 2px;
  }
  .venue-name {
    font-family: "Oswald", sans-serif;
    font-weight: 700;
    font-size: 46px;
    fill: var(--cream);
    text-anchor: middle;
    letter-spacing: 6px;
  }
  .label-kicker {
    font-family: "Oswald", sans-serif;
    font-weight: 700;
    font-size: 56px;
    fill: var(--pink);
    stroke: var(--plum);
    stroke-width: 8px;
    paint-order: stroke fill;
    text-anchor: middle;
  }
  .label-artists {
    font-family: "Bungee", sans-serif;
    font-size: 96px;
    fill: var(--sky);
    stroke: var(--plum);
    stroke-width: 12px;
    stroke-linejoin: round;
    paint-order: stroke fill;
    text-anchor: middle;
  }
</style>
</head>
<body>
<svg class="canvas" viewBox="0 0 1988 1851" preserveAspectRatio="none" xmlns="http://www.w3.org/2000/svg">
  <defs>
    <clipPath id="poster-clip"><rect x="314" y="118" width="1360" height="1614"/></clipPath>
    <radialGradient id="backdrop-glow" cx="0.5" cy="0.6" r="0.75">
      <stop offset="0" stop-color="var(--cream)"/>
      <stop offset="1" stop-color="var(--ray)"/>
    </radialGradient>
    <radialGradient id="record-tone" cx="994" cy="1735" r="598" gradientUnits="userSpaceOnUse">
      <stop offset="0.5" stop-color="var(--lemon)"/>
      <stop offset="0.6" stop-color="var(--vinyl)"/>
      <stop offset="1" stop-color="var(--vinyl)"/>
    </radialGradient>
    <path id="date-arc" d="M479 1735 A515 515 0 0 1 994 1220"/>
    <path id="venue-arc" d="M994 1220 A515 515 0 0 1 1509 1735"/>
  </defs>

  <g class="poster" clip-path="url(#poster-clip)">
    <rect class="backdrop" x="314" y="118" width="1360" height="1614" fill="url(#backdrop-glow)" role="img" aria-label="Sunburst rays behind the arch"/>

    <g class="arch-frame">
      <path d="M340 1732 V826 A654 654 0 0 1 1648 826 V1732 Z" fill="var(--pink)"/>
      <path d="M372 1732 V826 A622 622 0 0 1 1616 826 V1732 Z" fill="var(--plum)"/>
      <path d="M386 1732 V826 A608 608 0 0 1 1602 826 V1732 Z" fill="var(--sky)"/>
      <path d="M454 1732 V826 A540 540 0 0 1 1534 826 V1732 Z" fill="var(--cream)"/>
      <path d="M472 1732 V826 A522 522 0 0 1 1516 826 V1732 Z" fill="var(--plum)"/>
      <path d="M486 1732 V826 A508 508 0 0 1 1502 826 V1732 Z" fill="var(--pink)"/>
    </g>

    <g class="headline" transform="rotate(-8 980 700)">
      <text class="title title--top title-shadow" x="948" y="632">VELVET</text>
      <text class="title title--top title-fill--top" x="938" y="618">VELVET</text>
      <text class="title title--main title-shadow" x="994" y="902">TIDE</text>
      <text class="title title--main title-fill--main" x="982" y="884">TIDE</text>
    </g>

    <g class="ribbon" transform="rotate(-10 990 1000)">
      <polygon points="500,958 1490,958 1450,1008 1490,1058 500,1058 540,1008" fill="var(--lilac)"/>
      <text class="subtitle" x="990" y="1052">MUSIC PARTY</text>
    </g>

    <g class="record">
      <circle cx="994" cy="1735" r="622" fill="var(--cream)"/>
      <circle cx="994" cy="1735" r="598" fill="url(#record-tone)" role="img" aria-label="Vinyl record with a yellow centre label"/>

      <text class="venue-name" x="994" y="1200">BRUME7</text>

      <text class="record-text"><textPath href="#date-arc" startOffset="86%" text-anchor="end">SAMEDI 25 NOVEMBRE</textPath></text>
      <text class="record-text"><textPath href="#venue-arc" startOffset="14%">BRUME7 EVENT HALL</textPath></text>

      <text class="label-kicker" x="994" y="1510">SPECIAL</text>
      <text class="label-kicker" x="994" y="1568">PERFORMANCE</text>
      <text class="label-artists" x="994" y="1685">K-LENZ + MV</text>
    </g>
  </g>
</svg>
</body>
</html>
```